Luxury Brand Real Estate For Sale sign

**Update** I've added some examples from the internet of other signs that have a look similar to what I would like to see. I do not want my personal name in the sign. And the word FOR SALE Does not need to be so large - it can be more subtle.
I want to create a Real Estate for sale sign for my company that will be used for luxury/higher end real estate listings. I’m sharing my business card as well as a logo with new teal color to show what we're moving towards: we’re using Teal, white, black and gold.
Hoping the sign is simple, sophisticated and eye catching.
The sign should be 24" wide by 30" tall including the company name: Harbor Crest Realty Group and our logo, office phone number 727-555-0148 and website www.hcrgexample.com the words "For Sale"
Optional to add this e-mail address info@hcrgexample.com to the sign
Target Market(s)
Luxury home buyers
Industry/Entity Type
Real Estate
Look and feel

```html
<!DOCTYPE html>
<html lang="en">
<head>
<meta charset="utf-8">
<title>Harbor Crest Realty Group – For Sale</title>
<link href="https://fonts.googleapis.com/css2?family=Anton&family=Montserrat:wght@300;400;800&family=Saira+Stencil+One&display=swap" rel="stylesheet">
<style>
  :root {
    --teal: #128585;
    --ink: #000000;
    --graphite: #444444;
    --slate: #4a4a4a;
    --paper: #ffffff;
  }
  * { margin: 0; padding: 0; box-sizing: border-box; }
  html, body { width: 960px; height: 1200px; overflow: hidden; background: var(--paper); }
  .sign { position: relative; width: 960px; height: 1200px; background: var(--paper); overflow: hidden; }

  .corner-block { position: absolute; width: 96px; height: 97px; background: var(--teal); }
  .corner-block--top { left: 0; top: 0; }
  .corner-block--bottom { right: 0; bottom: 0; }

  .dot-grid { position: absolute; }
  .dot-grid--top { left: 824px; top: 48px; }
  .dot-grid--bottom { left: 58px; top: 1067px; }

  .brand-square {
    position: absolute; left: 186px; top: 149px;
    width: 89px; height: 89px;
    border: 4px solid var(--teal);
  }
  .brand-divider {
    position: absolute; left: 347px; top: 78px;
    width: 3px; height: 231px; background: var(--graphite);
  }
  .brand-name {
    position: absolute; left: 382px; top: 156px;
    font-family: 'Montserrat', sans-serif; font-weight: 400;
    color: var(--teal); font-size: 40px; line-height: 1;
    letter-spacing: 0.02em; text-transform: uppercase; white-space: nowrap;
  }
  .brand-tagline {
    position: absolute; left: 382px; top: 205px;
    font-family: 'Montserrat', sans-serif; font-weight: 300;
    color: var(--graphite); font-size: 25px; line-height: 1;
    letter-spacing: 0.62em; text-transform: uppercase; white-space: nowrap;
  }

  .frame { position: absolute; left: 97px; top: 392px; width: 766px; height: 558px; border: 1.5px solid var(--teal); }
  .frame-gap { position: absolute; left: 383px; width: 194px; height: 6px; background: var(--paper); }
  .frame-gap--top { top: 389px; }
  .frame-gap--bottom { top: 947px; }

  .quote-mark { position: absolute; left: 410px; width: 140px; height: 101px; }
  .quote-mark--open { top: 322px; }
  .quote-mark--close { top: 920px; }

  .headline {
    position: absolute; left: 0; top: 506px; width: 964px;
    text-align: center;
    font-family: 'Anton', sans-serif; font-size: 158px; line-height: 1;
    color: var(--ink); text-transform: uppercase; white-space: nowrap;
  }
  .accent-rule { position: absolute; height: 2px; background: var(--teal); }
  .accent-rule--left { left: 177px; top: 652px; width: 116px; }
  .accent-rule--right { left: 667px; top: 654px; width: 116px; }

  .phone {
    position: absolute; left: 0; top: 656px; width: 945px;
    text-align: center;
    font-family: 'Saira Stencil One', sans-serif; font-size: 96px; line-height: 1.1;
    color: var(--teal); white-space: nowrap;
  }
  .website {
    position: absolute; left: 0; top: 792px; width: 962px;
    text-align: center;
    font-family: 'Montserrat', sans-serif; font-weight: 800; font-size: 22px; line-height: 1;
    letter-spacing: 0.2em; color: var(--slate); text-transform: uppercase; white-space: nowrap;
  }
</style>
</head>
<body>
<main class="sign">
  <div class="corner-block corner-block--top"></div>
  <div class="corner-block corner-block--bottom"></div>

  <svg class="dot-grid dot-grid--top" width="80" height="100" viewBox="0 0 80 100" aria-hidden="true">
    <g fill="#128585">
      <circle cx="2.5" cy="2.5" r="2.3"/><circle cx="26.5" cy="2.5" r="2.3"/><circle cx="51" cy="2.5" r="2.3"/><circle cx="75" cy="2.5" r="2.3"/>
      <circle cx="2.5" cy="26" r="2.3"/><circle cx="26.5" cy="26" r="2.3"/><circle cx="51" cy="26" r="2.3"/><circle cx="75" cy="26" r="2.3"/>
      <circle cx="2.5" cy="50" r="2.3"/><circle cx="26.5" cy="50" r="2.3"/><circle cx="51" cy="50" r="2.3"/><circle cx="75" cy="50" r="2.3"/>
      <circle cx="2.5" cy="73.5" r="2.3"/><circle cx="26.5" cy="73.5" r="2.3"/><circle cx="51" cy="73.5" r="2.3"/><circle cx="75" cy="73.5" r="2.3"/>
      <circle cx="2.5" cy="97" r="2.3"/><circle cx="26.5" cy="97" r="2.3"/><circle cx="51" cy="97" r="2.3"/><circle cx="75" cy="97" r="2.3"/>
    </g>
  </svg>
  <svg class="dot-grid dot-grid--bottom" width="80" height="100" viewBox="0 0 80 100" aria-hidden="true">
    <g fill="#128585">
      <circle cx="2.5" cy="2.5" r="2.3"/><circle cx="26.5" cy="2.5" r="2.3"/><circle cx="51" cy="2.5" r="2.3"/><circle cx="75" cy="2.5" r="2.3"/>
      <circle cx="2.5" cy="26" r="2.3"/><circle cx="26.5" cy="26" r="2.3"/><circle cx="51" cy="26" r="2.3"/><circle cx="75" cy="26" r="2.3"/>
      <circle cx="2.5" cy="50" r="2.3"/><circle cx="26.5" cy="50" r="2.3"/><circle cx="51" cy="50" r="2.3"/><circle cx="75" cy="50" r="2.3"/>
      <circle cx="2.5" cy="73.5" r="2.3"/><circle cx="26.5" cy="73.5" r="2.3"/><circle cx="51" cy="73.5" r="2.3"/><circle cx="75" cy="73.5" r="2.3"/>
      <circle cx="2.5" cy="97" r="2.3"/><circle cx="26.5" cy="97" r="2.3"/><circle cx="51" cy="97" r="2.3"/><circle cx="75" cy="97" r="2.3"/>
    </g>
  </svg>

  <header class="brand">
    <div class="brand-square" aria-hidden="true"></div>
    <div class="brand-divider" aria-hidden="true"></div>
    <p class="brand-name">Harbor Crest</p>
    <p class="brand-tagline">Realty Group</p>
  </header>

  <div class="frame" aria-hidden="true"></div>
  <div class="frame-gap frame-gap--top" aria-hidden="true"></div>
  <div class="frame-gap frame-gap--bottom" aria-hidden="true"></div>

  <svg class="quote-mark quote-mark--open" viewBox="737 578 252 182" aria-hidden="true">
    <g fill="#128585">
      <path d="M747 645 L807 584 Q815 577 820 587 L794 642 Q791 655 800 655 L834 655 Q840 655 840 661 L840 751 Q840 757 834 757 L743 757 Q737 757 737 751 L737 668 Q737 655 747 645 Z"/>
      <path transform="translate(148 0)" d="M747 645 L807 584 Q815 577 820 587 L794 642 Q791 655 800 655 L834 655 Q840 655 840 661 L840 751 Q840 757 834 757 L743 757 Q737 757 737 751 L737 668 Q737 655 747 645 Z"/>
    </g>
  </svg>
  <svg class="quote-mark quote-mark--close" viewBox="737 578 252 182" aria-hidden="true">
    <g fill="#128585" transform="rotate(180 862.5 669)">
      <path d="M747 645 L807 584 Q815 577 820 587 L794 642 Q791 655 800 655 L834 655 Q840 655 840 661 L840 751 Q840 757 834 757 L743 757 Q737 757 737 751 L737 668 Q737 655 747 645 Z"/>
      <path transform="translate(148 0)" d="M747 645 L807 584 Q815 577 820 587 L794 642 Q791 655 800 655 L834 655 Q840 655 840 661 L840 751 Q840 757 834 757 L743 757 Q737 757 737 751 L737 668 Q737 655 747 645 Z"/>
    </g>
  </svg>

  <h1 class="headline">For Sale</h1>
  <div class="accent-rule accent-rule--left" aria-hidden="true"></div>
  <div class="accent-rule accent-rule--right" aria-hidden="true"></div>
  <p class="phone">727-555-0148</p>
  <p class="website">www.hcrgexample.com</p>
</main>
</body>
</html>
```